Business Card Design Project

I need a business card design for our new logo, please check the logo at the following link:
https://www.filecrate.net/s/q7rtx2pw9kd41m/FernLoop.png
The address on the business card:
Av. Gervásio Tavares 418 sala 207
Barra da Tijuca, Rio de Janeiro, RJ
CEP: 22714-380
Brasil
Phone: +55 21 86347215
e-mail: osvaldo@fernloop.com.br
Updates
Thank you all for sending your designs, we will not provide feedback because there are too many designs, on December 3 we will pick the best design according to our point of view. Please keep posting.
Osvaldo
Industry/Entity Type
Business
Look and feel
Each slider illustrates characteristics of the customer's brand and the style your logo design should communicate.

```html
<!DOCTYPE html>
<html lang="pt-BR">
<head>
<meta charset="utf-8">
<title>FernLoop — Business Card</title>
<link rel="stylesheet" href="https://fonts.googleapis.com/css2?family=Arimo:ital,wght@0,400;0,700;1,400&display=swap">
<style>
  :root {
    --backdrop: #fbb558;
    --card-dark: #1e1e1e;
    --brand-yellow: #f5c400;
    --pill-white: #ffffff;
    --ink: #1e1e1e;
  }
  * { margin: 0; padding: 0; box-sizing: border-box; }
  html, body {
    width: 1200px;
    height: 1000px;
    overflow: hidden;
    background: var(--backdrop);
    font-family: "Arimo", Arial, sans-serif;
  }
  .canvas {
    position: relative;
    width: 1200px;
    height: 1000px;
  }
  .card {
    position: absolute;
    width: 798px;
    height: 443px;
    background: var(--card-dark);
    overflow: hidden;
  }
  .card--front { left: 60px; top: 44px; }
  .card--back { left: 357px; top: 517px; }

  .ring {
    position: absolute;
    inset: 0;
    width: 798px;
    height: 443px;
  }

  .logo-pill {
    position: absolute;
    width: 237px;
    height: 150px;
    border-radius: 75px;
    background: var(--pill-white);
    display: flex;
    align-items: center;
    justify-content: center;
    gap: 10px;
  }
  .card--front .logo-pill { left: 73px; top: 40px; }
  .card--back .logo-pill { left: 283px; top: 145px; }

  .logo-mark {
    width: 22px;
    height: 22px;
    border-radius: 50%;
    background: var(--brand-yellow);
  }
  .logo-name {
    font-weight: 700;
    font-size: 30px;
    color: var(--ink);
    letter-spacing: 0.2px;
  }

  .contact {
    position: absolute;
    left: 514px;
    top: 186px;
    color: var(--brand-yellow);
    font-size: 14.5px;
    line-height: 22.7px;
  }
  .contact address { font-style: normal; }
  .contact .reach { margin-top: 45px; }
  .contact .label { font-style: italic; }

  .band {
    position: absolute;
    left: 0;
    top: 193px;
    width: 100%;
    height: 47px;
    background: var(--brand-yellow);
  }
</style>
</head>
<body>
<main class="canvas">

  <section class="card card--front" aria-label="Business card front">
    <svg class="ring" viewBox="0 0 798 443" aria-hidden="true">
      <circle cx="650" cy="256" r="264.5" fill="none" stroke="var(--brand-yellow)" stroke-width="60"/>
    </svg>

    <div class="logo-pill">
      <span class="logo-mark"></span>
      <span class="logo-name">FernLoop</span>
    </div>

    <div class="contact">
      <address>
        Av. Gervásio Tavares 418 sala 207<br>
        Barra da Tijuca, Rio de Janeiro, RJ<br>
        CEP: 22714-380<br>
        Brasil
      </address>
      <p class="reach">
        <span class="label">Phone:</span> +55 21 86347215<br>
        <span class="label">e-mail:</span> osvaldo@fernloop.com.br
      </p>
    </div>
  </section>

  <section class="card card--back" aria-label="Business card back">
    <div class="band"></div>
    <div class="logo-pill">
      <span class="logo-mark"></span>
      <span class="logo-name">FernLoop</span>
    </div>
  </section>

</main>
</body>
</html>
```